Real Estate - Property Management Prospectus/Brochure

We need a prospectus made up, around 9-10 pages including the cover page pages 3 onwards can be all a similar template happy for the front cover to have lots of black. I would like it to look very classy and futuristic, high end, blacks, silvers and whites, i am specializing in managing high end rental properties. i would like to design to correspond with the logo. I need to be able to email this booklet mostly - and also be able to print and mail out as well. I would like it crisp and clean as well - not to much on a page. Please note - happy for the cover to be simple with the logo added - prefer lots of black and with the other pages - they can all be a similar layout template to make this job easier? My website is www.tallowquay.com.au and phone is 0471 382 519 email is morva@tallowquay.com.au
Target Market(s)
Investors
Industry/Entity Type
Real Estate
Requirements
Should not have
- Bright greens or bold colours

```html
<!DOCTYPE html>
<html lang="en">
<head>
<meta charset="utf-8">
<title>Tallowquay Prospectus Cover Spread</title>
<link rel="stylesheet" href="https://fonts.googleapis.com/css2?family=Oswald:wght@300;400;500&family=Montserrat:wght@800&display=swap">
<style>
  :root {
    --backdrop: #d9d6d2;
    --black: #0b0b0b;
    --ink: #1a1a1a;
    --white: #ffffff;
    --silver: #c9c9c9;
    --silver-light: #eeeeee;
    --grey-text: #9a9a9a;
    --muted: #bdbdbd;
  }
  * { box-sizing: border-box; margin: 0; padding: 0; }
  html, body { width: 1200px; height: 907px; overflow: hidden; }
  body { background: var(--backdrop); position: relative; font-family: "Oswald", sans-serif; }

  .spread {
    position: absolute; left: 100px; top: 103px;
    width: 1000px; height: 700px;
    display: flex;
    box-shadow: 0 10px 30px rgba(0,0,0,.25);
  }
  .page { position: relative; width: 500px; height: 700px; overflow: hidden; background: var(--black); }

  /* Back cover */
  .back-cover__skyline {
    position: absolute; left: 0; top: 0; width: 500px; height: 560px;
    background: linear-gradient(170deg, #fafafa 0%, #e4e4e4 40%, #cfcfcf 75%, #e9e9e9 100%);
    border-bottom: 6px solid var(--silver);
  }
  .back-cover__footer {
    position: absolute; left: 0; bottom: 0; width: 500px; height: 134px;
    padding: 40px 0 0 36px; color: var(--white);
  }
  .contact-list { list-style: none; }
  .contact-list li { display: flex; align-items: center; gap: 8px; font-size: 14px; font-weight: 300; line-height: 22px; }
  .contact-list li.contact-phone { font-size: 19px; font-weight: 400; line-height: 26px; }
  .contact-list svg { width: 11px; height: 11px; flex: none; }
  .social { position: absolute; left: 300px; top: 20px; }
  .social__label { font-size: 12px; font-weight: 400; color: var(--white); margin-bottom: 8px; }
  .social__icons { display: flex; gap: 10px; }
  .social__icons span { width: 16px; height: 16px; border-radius: 50%; background: var(--white); }

  /* Front cover */
  .front-cover__top {
    position: absolute; left: 0; top: 0; width: 500px; height: 250px;
    background: linear-gradient(180deg, #f3f3f3 0%, #e2e2e2 100%);
  }
  .front-cover__bottom {
    position: absolute; left: 0; top: 250px; width: 500px; height: 450px;
    background: linear-gradient(180deg, #151515 0%, var(--black) 100%);
    border-top: 4px solid var(--silver);
  }
  .brand {
    position: absolute; left: 40px; top: 30px; width: 210px; text-align: center;
  }
  .brand__box {
    border: 2px solid var(--ink); padding: 6px 10px;
    display: flex; align-items: center; justify-content: center; gap: 8px;
  }
  .brand__mark { width: 10px; height: 10px; background: var(--ink); }
  .brand__name { font-size: 24px; font-weight: 400; letter-spacing: 2px; color: var(--ink); text-transform: uppercase; }
  .brand__url { margin-top: 4px; font-size: 10px; letter-spacing: 3px; color: var(--ink); text-transform: uppercase; }

  .feature-photo { position: absolute; left: 160px; top: 40px; }

  .headline { position: absolute; left: 50px; top: 505px; color: var(--white); text-transform: uppercase; }
  .headline__lead { font-family: "Montserrat", sans-serif; font-weight: 800; font-size: 21px; letter-spacing: .5px; }
  .headline__line { font-weight: 400; font-size: 21px; color: var(--grey-text); line-height: 28px; }
  .headline__focus { font-weight: 500; font-size: 30px; color: var(--muted); line-height: 34px; }
  .headline__call { margin-top: 10px; font-weight: 400; font-size: 13px; letter-spacing: 5px; color: var(--white); }
</style>
</head>
<body>
  <main class="spread">
    <section class="page back-cover">
      <div class="back-cover__skyline" role="img" aria-label="Faded grey aerial photograph of a coastal city skyline with high-rise towers and beach"></div>
      <footer class="back-cover__footer">
        <ul class="contact-list">
          <li class="contact-phone">
            <svg viewBox="0 0 12 12"><circle cx="6" cy="6" r="5.5" fill="none" stroke="#fff"/><path d="M4 3.5l1 1.2-.6.8c.4.8 1 1.4 1.8 1.8l.8-.6 1.2 1-.7 1c-2.4-.4-4-2-4.4-4.4z" fill="#fff"/></svg>
            0471 382 519
          </li>
          <li>
            <svg viewBox="0 0 12 12"><circle cx="6" cy="6" r="5.5" fill="#fff"/></svg>
            www.tallowquay.com.au
          </li>
          <li>
            <svg viewBox="0 0 12 12"><rect x="1" y="3" width="10" height="7" fill="#fff"/><path d="M1 3l5 4 5-4" fill="none" stroke="#0b0b0b"/></svg>
            morva@tallowquay.com.au
          </li>
        </ul>
        <div class="social">
          <p class="social__label">like us</p>
          <div class="social__icons"><span></span><span></span><span></span><span></span></div>
        </div>
      </footer>
    </section>

    <section class="page front-cover">
      <div class="front-cover__top"></div>
      <div class="front-cover__bottom"></div>

      <div class="brand">
        <div class="brand__box">
          <span class="brand__mark"></span>
          <span class="brand__name">tallowquay</span>
        </div>
        <p class="brand__url">www.tallowquay.com.au</p>
      </div>

      <svg class="feature-photo" width="420" height="440" viewBox="0 0 420 440">
        <defs>
          <linearGradient id="photoTone" x1="0" y1="0" x2="0" y2="1">
            <stop offset="0" stop-color="#8fb8e0"/>
            <stop offset=".5" stop-color="#5d8fb0"/>
            <stop offset=".75" stop-color="#6f7780"/>
            <stop offset="1" stop-color="#3f4348"/>
          </linearGradient>
          <linearGradient id="ringTone" x1="0" y1="0" x2="1" y2="1">
            <stop offset="0" stop-color="#111"/>
            <stop offset=".5" stop-color="#9a9a9a"/>
            <stop offset="1" stop-color="#f2f2f2"/>
          </linearGradient>
        </defs>
        <circle cx="215" cy="215" r="212" fill="url(#ringTone)"/>
        <circle cx="215" cy="215" r="198" fill="url(#photoTone)" role="img" aria-label="Photograph of a modern glass office building with an empty car park under a blue sky"/>
      </svg>

      <div class="headline">
        <p class="headline__lead">Morva is an industry</p>
        <p class="headline__line">expert with a history of excellence</p>
        <p class="headline__focus">in property management</p>
        <p class="headline__call">Call today 0471 382 519</p>
      </div>
    </section>
  </main>
</body>
</html>
```